依頼詳細
アルコール除菌ジェルのラベルのデザインをお願い致します
記載項目
サイズはW110mm×H154mm
ラミネート貼り
希望イメージ
シンプル 複雑
単色 カラフル
暗い 明るい
日常 高級
遊び心 厳粛
未来的 伝統的
女性的 男性的
希望する色
緑系
納品ファイル
• イラストレーター形式 (.ai)
補足説明
実際の現在のデザイン(他社)を添付致します。
添付のデザインのOEM製品になり弊社自社品となります
雰囲気を全然違うようにしてください
業務用です
添付の画像にありますQELTは必要ございません
また発売元は弊社で製造元は別な会社で記載頂くと思います
宜しくお願い致します
容器の画像を添付致しました。
円形のPETボトルになります
販売先は自動車ディーラー様中心となります

ディーラー様及び通常の販売先において頂けるデザインでした
関係者で3点選びましたが、全員がこの方のデザインが上がりましたので
決定しました

沢山の方からデザインをあげて頂き非常に迷いました。
今後もこのサイトを使って新商品のデザインや
容器のデザインをお願いしたいと思いますのでその際は
宜しいお願い致します。今回はありがとうございました

```html
<!DOCTYPE html>
<html lang="ja">
<head>
<meta charset="utf-8">
<title>アルコール除菌ジェル ラベル</title>
<link href="https://fonts.googleapis.com/css2?family=Cormorant+Garamond:wght@600&family=M+PLUS+1p:wght@500;800&display=swap" rel="stylesheet">
<style>
  :root {
    --green: #1f5c3c;
    --green-dark: #12432a;
    --green-light: #3f8060;
    --mist-1: #e2e8e5;
    --mist-2: #f5f7f6;
    --white: #ffffff;
  }
  html, body { margin: 0; padding: 0; overflow: hidden; }
  body { width: 1200px; height: 1181px; }
  .label {
    position: relative;
    width: 1200px; height: 1181px;
    background: linear-gradient(90deg, var(--mist-1), var(--mist-2) 50%, var(--mist-1));
    overflow: hidden;
  }
  .rule { position: absolute; left: 0; width: 100%; background: var(--green); }
  .rule--top { top: 50px; height: 5px; }
  .rule--bottom { top: 147px; height: 5px; }
  .title-band {
    position: absolute; top: 58px; left: 0; width: 100%; height: 84px;
    background: linear-gradient(180deg, var(--green-light), var(--green) 40%, var(--green-dark));
    display: flex; align-items: center; justify-content: center;
  }
  .title-band__text {
    font-family: "Cormorant Garamond", serif;
    font-weight: 600; font-size: 46px; letter-spacing: 2px;
    color: var(--white); margin: 0;
  }
  .cross-mark { position: absolute; left: 484px; top: 198px; width: 232px; height: 232px; }
  .name-panel {
    position: absolute; top: 474px; left: 0; width: 100%; height: 536px;
    background: var(--white);
    display: flex; flex-direction: column; align-items: center; justify-content: center;
  }
  .product-name {
    margin: 0;
    font-family: "M PLUS 1p", sans-serif; font-weight: 500;
    font-size: 172px; line-height: 220px; letter-spacing: 6px;
    color: var(--green); text-align: center;
    text-shadow: -1px -1px 0 var(--green-light), 2px 3px 0 var(--green-dark), 4px 6px 8px rgba(0,0,0,0.25);
  }
  .product-name span { display: block; }
  .info-row {
    position: absolute; top: 1040px; left: 0; width: 100%;
    display: flex; justify-content: center; gap: 38px;
  }
  .badge { display: flex; flex-direction: column; align-items: center; }
  .badge svg { width: 90px; height: 90px; }
  .badge__caption {
    font-family: "M PLUS 1p", sans-serif; font-weight: 800;
    font-size: 13px; color: var(--green-dark); margin-top: 10px;
  }
</style>
</head>
<body>
  <div class="label">
    <div class="rule rule--top"></div>
    <header class="title-band"><h2 class="title-band__text">Alcohol Sterilizing Gel</h2></header>
    <div class="rule rule--bottom"></div>

    <svg class="cross-mark" viewBox="0 0 232 232" aria-hidden="true">
      <defs>
        <linearGradient id="ring" x1="0" y1="0" x2="1" y2="1">
          <stop offset="0" stop-color="#3f8060"/><stop offset="1" stop-color="#12432a"/>
        </linearGradient>
      </defs>
      <circle cx="116" cy="116" r="110" fill="none" stroke="url(#ring)" stroke-width="7"/>
      <circle cx="116" cy="116" r="98" fill="#eef2f0" stroke="#1f5c3c" stroke-width="3"/>
      <path d="M96 46h40v50h50v40h-50v50h-40v-50h-50v-40h50z" fill="url(#ring)" stroke="#12432a" stroke-width="2"/>
    </svg>

    <section class="name-panel">
      <h1 class="product-name"><span>アルコール</span><span>除菌ジェル</span></h1>
    </section>

    <div class="info-row">
      <div class="badge">
        <svg viewBox="0 0 90 90" aria-label="容量 1ℓ" role="img">
          <circle cx="45" cy="45" r="41" fill="#fff" stroke="#1f5c3c" stroke-width="6"/>
          <text x="45" y="58" text-anchor="middle" font-family="M PLUS 1p, sans-serif" font-weight="800" font-size="38" fill="#1f5c3c">1ℓ</text>
        </svg>
      </div>
      <div class="badge">
        <svg viewBox="0 0 90 90" aria-label="火気厳禁" role="img">
          <circle cx="45" cy="45" r="41" fill="#fff" stroke="#1f5c3c" stroke-width="6"/>
          <path d="M45 16c5 9 14 15 14 26a14 14 0 0 1-28 0c0-7 5-10 7-16 3 5 3 9 7 10-1-7-2-13 0-20z" fill="none" stroke="#1f5c3c" stroke-width="3"/>
          <path d="M28 20l34 36M62 20l-34 36" stroke="#1f5c3c" stroke-width="3"/>
          <text x="45" y="71" text-anchor="middle" font-family="M PLUS 1p, sans-serif" font-weight="800" font-size="11" fill="#12432a">火気厳禁</text>
        </svg>
        <span class="badge__caption">エタノール含有</span>
      </div>
    </div>
  </div>
</body>
</html>
```